Smart Home App Needs 4 Mockup Screens. Extra Work Guaranteed for Winner

BACKGROUND
Our company, Lumora, is launching an exciting new app early next year. And we need some examples of what our app will look like to show to some of the biggest retailers in the world. We hope that this project will lead to regular work as we have a lot of new products planned for the app.

Our app will support baby, home and pet monitors (cameras) as well as the world's first smart pet flap.

The monitors allow you to do much more than just watch live video. By monitoring and providing information on sound, movement and temperature the app provides the user with instant peace of mind wherever they are. If anything has changed the user can be alerted via notifications. If motion is detected the user will receive a clip of the whole event moments after it has happened.

The Smart Pet Flap is packed full of features too. From letting you decide when your pet can or can't go outside from your mobile, to automatically opening if a fire is detected (along with a whole host of other features) - this really is the most advanced pet flap in the world.

REQUIREMENTS
We need 4 mock-up screens creating to show the UI of our app.
1. Camera Home Page
2. Camera Notifications Page
3. Pet Flap Fire Alarm Warning Page
4. Extreme Weather Warning Page

Optional - Happy to Pay the Winner Extra for these Designs
5. Start Up/Log In Page
6. Pet Flap Notification Example
7. Pet Flap Scheduler Page (your choice)
(SEE LUMORA APP DESIGN COMPETITION - ATTACHED)

STYLE GUIDE
As you'll see from our wireframes we want our app to be very minimal and modern. The predominant colour will be white but where colour is used it should be bright (see our colour palette - which we will provide shortly).

INSPIRATION
We love the UI of Finchly (home surveillance). Also check out Vesk (smart thermostat).
(SEE LUMORA UI EXAMPLES ATTACHED)

LOGO
We love our logo. Feel free to use it in creative ways.

So far we're also using it as a kind of beacon to indicate if everything is ok.

LOGO COLOURS & APP COLOURS
As mentioned, we are thinking of using the green logo to indicate that everything is ok (and also for the pet app in general). We reserve red for when something has happened (normally bad) and needs attention, like a fire alarm going off.

The app will be predominantly black and white with the odd minimal flash of colour (probably primary colour)
We'll upload a colour scheme as soon as we have it.

CONTACT
Please message us for more details - we'll do our best to reply promptly.

FUTURE WORK
We will need extra screens made straight after the competition is over and there should be additional regular work after this.

Target Market(s)

Our app will be used by young professionals, to young parents to grandparents. The design must be contemporary but timeless and easy to use no matter how good you are with technology.

Industry/Entity Type

Pet

Font styles to use
Sans Serif

Colors
faee3f
33a6d7
ec1f27
acd036
32b7a4

Requirements
Must have
• Beautiful, minimal design. Make sure you spend time looking at the Finchly and Vesk apps before starting.

For the videos make sure you use sensible images - that you'd expect to see from a monitor (high resolution images if possible)
Nice to have
• Creative use of our logo.
Should not have
• Too much detail/clutter/colours. Ugly fonts.

```html
<!DOCTYPE html>
<html lang="en">
<head>
<meta charset="utf-8">
<title>Lumora – Camera Home</title>
<link href="https://fonts.googleapis.com/css2?family=Open+Sans:wght@400;600;700&display=swap" rel="stylesheet">
<style>
:root{
  --backdrop:#4aa8e0;
  --screen-white:#ffffff;
  --status-dark:#2b2d30;
  --teal:#32b7a4;
  --teal-tile:rgba(255,255,255,.2);
  --grid-grey:#e7e8e9;
  --tabbar-grey:#a9b4ba;
  --tabbar-line:#bcc5ca;
  --text-dark:#3a3d40;
  --text-muted:#8a8f94;
  --alert-red:#ec1f27;
  --blanket-blue:#b9cde6;
  --sheet-white:#f4f6f8;
  --linen:#e9e4dc;
  --warm-skin:#efd7c6;
  --room-white:#f3f4f4;
  --room-grey:#b9bec1;
  --room-shadow:#8f9599;
  --foliage:#a7b09a;
  --stone:#c9c2b6;
  --sky:#e8eef2;
}
*{box-sizing:border-box;margin:0;padding:0}
html,body{width:1200px;height:900px;overflow:hidden}
body{background:var(--backdrop);font-family:"Open Sans",sans-serif;position:relative}
.app-screen{position:absolute;left:370px;top:42px;width:460px;height:816px;background:var(--screen-white);display:flex;flex-direction:column;overflow:hidden;box-shadow:0 10px 30px rgba(0,0,0,.12)}
.status-bar{height:28px;background:var(--status-dark);color:#fff;display:flex;align-items:center;justify-content:space-between;padding:0 10px;font-size:13px;font-weight:600}
.status-bar .carrier,.status-bar .power{display:flex;align-items:center;gap:6px}
.app-header{height:56px;display:flex;align-items:center;justify-content:space-between;padding:0 0 0 18px}
.view-tabs{display:flex;height:100%}
.view-tab{width:90px;display:flex;align-items:center;justify-content:center;font-size:10px;font-weight:700;letter-spacing:.08em;color:var(--text-dark)}
.view-tab.is-active{box-shadow:inset 0 -3px 0 var(--teal)}
.live-feed{height:230px;background:
  radial-gradient(ellipse 22% 30% at 66% 52%, var(--warm-skin) 0%, rgba(239,215,198,0) 100%),
  radial-gradient(ellipse 45% 60% at 18% 30%, var(--linen) 0%, rgba(233,228,220,0) 100%),
  radial-gradient(ellipse 40% 45% at 50% 55%, var(--sheet-white) 0%, rgba(244,246,248,0) 100%),
  linear-gradient(135deg, #e6ebf1 0%, var(--blanket-blue) 100%)}
.control-band{height:110px;background:var(--teal);display:flex;justify-content:space-around;align-items:center;padding:0 10px}
.control{display:flex;flex-direction:column;align-items:center;gap:8px;color:#fff;font-size:9px;font-weight:700;letter-spacing:.06em}
.control-tile{width:56px;height:48px;background:var(--teal-tile);display:flex;align-items:center;justify-content:center}
.camera-grid{flex:1;background:var(--grid-grey);display:grid;grid-template-columns:1fr 1fr;gap:14px;padding:14px}
.camera-card{background:#fff;display:flex;flex-direction:column}
.camera-card .snapshot{flex:1}
.snapshot.nursery{background:
  radial-gradient(ellipse 40% 50% at 30% 30%, #ffffff 0%, rgba(255,255,255,0) 100%),
  radial-gradient(ellipse 35% 45% at 75% 65%, #dfe5e3 0%, rgba(223,229,227,0) 100%),
  linear-gradient(160deg, var(--room-white) 0%, #d4dad8 100%)}
.snapshot.patio{background:
  radial-gradient(ellipse 45% 35% at 60% 15%, var(--sky) 0%, rgba(232,238,242,0) 100%),
  radial-gradient(ellipse 30% 40% at 15% 70%, var(--foliage) 0%, rgba(167,176,154,0) 100%),
  linear-gradient(170deg, #d9d6d0 0%, var(--stone) 55%, var(--room-shadow) 100%)}
.snapshot.living{background:
  radial-gradient(ellipse 40% 45% at 70% 30%, #ffffff 0%, rgba(255,255,255,0) 100%),
  radial-gradient(ellipse 35% 30% at 30% 75%, var(--room-shadow) 0%, rgba(143,149,153,0) 100%),
  linear-gradient(160deg, #e4e6e7 0%, var(--room-grey) 100%)}
.snapshot.kitchen{background:
  radial-gradient(ellipse 40% 40% at 55% 30%, #ffffff 0%, rgba(255,255,255,0) 100%),
  radial-gradient(ellipse 30% 30% at 85% 80%, #a9aeb1 0%, rgba(169,174,177,0) 100%),
  linear-gradient(160deg, var(--room-white) 0%, #c6cacc 100%)}
.camera-card .label{height:32px;display:flex;align-items:center;gap:8px;padding:0 10px;font-size:11px;color:var(--text-muted)}
.tab-bar{height:72px;background:var(--tabbar-grey);display:flex}
.tab-item{flex:1;display:flex;align-items:center;justify-content:center;border-left:1px solid var(--tabbar-line);position:relative}
.tab-item:first-child{border-left:none}
.badge{position:absolute;top:20px;left:calc(50% + 6px);width:12px;height:12px;border-radius:50%;background:var(--alert-red);color:#fff;font-size:8px;font-weight:700;display:flex;align-items:center;justify-content:center}
</style>
</head>
<body>
<main class="app-screen">
  <div class="status-bar">
    <span class="carrier">
      <svg width="22" height="10" viewBox="0 0 22 10" fill="#fff"><rect x="0" y="7" width="3" height="3"/><rect x="4.5" y="5" width="3" height="5"/><rect x="9" y="3" width="3" height="7"/><rect x="13.5" y="1" width="3" height="9"/><rect x="18" y="0" width="3" height="10"/></svg>
      DINE
    </span>
    <span class="clock">10:35 AM</span>
    <span class="power">
      <svg width="11" height="11" viewBox="0 0 12 12"><circle cx="6" cy="6" r="5" fill="none" stroke="#fff" stroke-width="1.5"/><path d="M6 3v3l2 1.5" stroke="#fff" stroke-width="1.4" fill="none"/></svg>
      65%
      <svg width="24" height="11" viewBox="0 0 24 11"><rect x=".5" y=".5" width="20" height="10" rx="1.5" fill="none" stroke="#fff"/><rect x="2" y="2" width="12" height="7" fill="#fff"/><rect x="21" y="3.5" width="2" height="4" fill="#fff"/></svg>
    </span>
  </div>

  <header class="app-header">
    <svg class="menu-icon" width="22" height="16" viewBox="0 0 22 16" fill="var(--text-dark)"><rect x="0" y="1" width="3" height="2"/><rect x="5" y="1" width="17" height="2"/><rect x="0" y="7" width="3" height="2"/><rect x="5" y="7" width="17" height="2"/><rect x="0" y="13" width="3" height="2"/><rect x="5" y="13" width="17" height="2"/></svg>
    <nav class="view-tabs">
      <span class="view-tab is-active">NOW</span>
      <span class="view-tab">TRENDS</span>
    </nav>
  </header>

  <div class="live-feed" role="img" aria-label="Live nursery camera feed of a baby sleeping in a cot under a checked blanket"></div>

  <section class="control-band">
    <div class="control">
      <div class="control-tile"><svg width="22" height="26" viewBox="0 0 22 26" fill="none" stroke="#fff" stroke-width="2"><rect x="7" y="1" width="8" height="14" rx="4" fill="#fff"/><path d="M3 11a8 8 0 0 0 16 0M11 19v5M7 24h8"/></svg></div>
      SPEAK
    </div>
    <div class="control">
      <div class="control-tile"><svg width="18" height="28" viewBox="0 0 18 28" fill="#fff"><rect x="6" y="1" width="6" height="17" rx="3"/><circle cx="9" cy="21" r="6"/></svg></div>
      TEMPERATURE
    </div>
    <div class="control">
      <div class="control-tile"><svg width="28" height="24" viewBox="0 0 28 24" stroke="#fff" stroke-width="2" fill="#fff"><path d="M4 2v20M11 2v20M18 2v20M25 2v20"/><rect x="1" y="13" width="6" height="3"/><rect x="8" y="6" width="6" height="3"/><rect x="15" y="15" width="6" height="3"/><rect x="22" y="8" width="6" height="3"/></svg></div>
      CHECK DATA
    </div>
    <div class="control">
      <div class="control-tile"><svg width="26" height="26" viewBox="0 0 26 26" fill="none" stroke="#fff" stroke-width="2.4"><path d="M2 9V2h7M2 2l7 7M24 9V2h-7M24 2l-7 7M2 17v7h7M2 24l7-7M24 17v7h-7M24 24l-7-7"/></svg></div>
      ZOOM
    </div>
  </section>

  <section class="camera-grid">
    <article class="camera-card">
      <div class="snapshot nursery" role="img" aria-label="Nursery camera still of a white nursery with shelving"></div>
      <div class="label"><svg width="12" height="8" viewBox="0 0 12 8" fill="var(--text-muted)"><rect width="8" height="8" rx="1"/><path d="M8 3l4-2v6L8 5z"/></svg>Nursery camera</div>
    </article>
    <article class="camera-card">
      <div class="snapshot patio" role="img" aria-label="Patio camera still of the house exterior and patio"></div>
      <div class="label"><svg width="12" height="8" viewBox="0 0 12 8" fill="var(--text-muted)"><rect width="8" height="8" rx="1"/><path d="M8 3l4-2v6L8 5z"/></svg>Patio camera</div>
    </article>
    <article class="camera-card">
      <div class="snapshot living" role="img" aria-label="Living room camera still of a bright living room with sofa"></div>
      <div class="label"><svg width="12" height="8" viewBox="0 0 12 8" fill="var(--text-muted)"><rect width="8" height="8" rx="1"/><path d="M8 3l4-2v6L8 5z"/></svg>Living room camera</div>
    </article>
    <article class="camera-card">
      <div class="snapshot kitchen" role="img" aria-label="Kitchen camera still of a white kitchen with windows"></div>
      <div class="label"><svg width="12" height="8" viewBox="0 0 12 8" fill="var(--text-muted)"><rect width="8" height="8" rx="1"/><path d="M8 3l4-2v6L8 5z"/></svg>Kitchen camera</div>
    </article>
  </section>

  <nav class="tab-bar">
    <div class="tab-item"><svg width="22" height="22" viewBox="0 0 22 22" fill="#fff"><circle cx="11" cy="6" r="5"/><path d="M1 22a10 8 0 0 1 20 0z"/></svg></div>
    <div class="tab-item"><svg width="24" height="20" viewBox="0 0 24 20" fill="none" stroke="#fff" stroke-width="2"><path d="M2 5h5l2-3h6l2 3h5v13H2z"/><circle cx="12" cy="11" r="4"/></svg></div>
    <div class="tab-item"><svg width="22" height="22" viewBox="0 0 24 24" fill="#fff"><path d="M10 1h4l.6 3 2.4 1 2.6-1.7 2.8 2.8L20.7 8.7l1 2.4 3 .6v4l-3 .6-1 2.4 1.7 2.6-2.8 2.8-2.6-1.7-2.4 1-.6 3h-4l-.6-3-2.4-1-2.6 1.7-2.8-2.8 1.7-2.6-1-2.4-3-.6v-4l3-.6 1-2.4L1.7 6.1 4.5 3.3 7.1 5l2.4-1z" transform="scale(.92) translate(1 1)"/><circle cx="12" cy="12" r="4" fill="var(--tabbar-grey)"/></svg></div>
    <div class="tab-item"><svg width="22" height="22" viewBox="0 0 22 22" fill="none" stroke="#fff" stroke-width="2"><circle cx="11" cy="11" r="9"/><path d="M2 11h18M11 2c-4 5-4 13 0 18M11 2c4 5 4 13 0 18"/></svg><span class="badge">3</span></div>
  </nav>
</main>
</body>
</html>
```